hotel amenities supply company needs design for bottles and accessories

we need to design four 30ml amenity tubes branded "ORVENTA" , shampoo, shower gel, conditioner and body lotion. the bottle has to be somewhat clear to be able to see the liquid inside. its basically designing the complete identity for "orventa". attached are some examples. also the accessory boxes should match the design eg, shaving kit,vanity kit, toothbrush etc

Target Market(s)

hotels

Industry/Entity Type

Hotel

Font styles to use
Script

Requirements
Must have
• name "orventa " on bottles and product info
Should not have
• dark colors

```html
<!DOCTYPE html>
<html lang="en">
<head>
<meta charset="utf-8">
<title>Orventa Amenity Tubes</title>
<link href="https://fonts.googleapis.com/css2?family=Raleway:wght@300&display=swap" rel="stylesheet">
<style>
  :root {
    --bg-top: #5a5a5a;
    --bg-bottom: #c4c4c4;
    --tube: #dcdcdc;
    --seal: #c9c9c9;
    --seal-line: #b0b0b0;
    --cap: #f4f4f4;
    --brand: #2f8a80;
    --band: #1f6456;
    --band-text: #d8e6df;
    --leaf-a: rgba(31, 100, 86, 0.28);
    --leaf-b: rgba(47, 138, 128, 0.10);
    --fill-shampoo: #c9c8a8;
    --fill-conditioner: #d2d2d2;
    --fill-shower: #dedcb2;
    --fill-lotion: #b2e2e2;
  }
  * { box-sizing: border-box; margin: 0; padding: 0; }
  html, body { width: 1200px; height: 640px; overflow: hidden; }
  body { background: linear-gradient(180deg, var(--bg-top), var(--bg-bottom)); }

  .range { position: relative; width: 1200px; height: 640px; }

  .tube { position: absolute; top: 88px; width: 220px; height: 502px; }
  .tube--shampoo { left: 114px; }
  .tube--conditioner { left: 367px; }
  .tube--shower { left: 620px; }
  .tube--lotion { left: 874px; }

  .tube__seal {
    position: absolute; top: 0; left: 0; width: 220px; height: 14px;
    background: repeating-linear-gradient(90deg, var(--seal) 0 3px, var(--seal-line) 3px 4px);
    border-radius: 3px 3px 0 0;
  }
  .tube__body {
    position: absolute; top: 14px; left: 0; width: 220px; height: 446px;
    background: var(--tube);
    clip-path: polygon(0 0, 100% 0, 83% 100%, 17% 100%);
    overflow: hidden;
  }
  .tube__fill { position: absolute; left: 0; right: 0; top: 72px; bottom: 0; }
  .tube--shampoo .tube__fill { background: var(--fill-shampoo); }
  .tube--conditioner .tube__fill { background: var(--fill-conditioner); }
  .tube--shower .tube__fill { background: var(--fill-shower); }
  .tube--lotion .tube__fill { background: var(--fill-lotion); }

  .tube__vine {
    position: absolute; left: 14px; top: 14px; width: 60px; height: 250px;
    background: radial-gradient(ellipse at 50% 50%, var(--leaf-a), var(--leaf-b) 70%, transparent);
    border-radius: 40%;
  }
  .tube__sprig {
    position: absolute; left: 58px; top: 282px; width: 78px; height: 124px;
    background: radial-gradient(ellipse at 50% 50%, var(--leaf-a), var(--leaf-b) 70%, transparent);
    border-radius: 45%;
  }

  .tube__brand {
    position: absolute; left: 62px; top: 76px;
    font-family: "Raleway", sans-serif; font-weight: 300;
    font-size: 30px; letter-spacing: 1px;
    color: var(--brand); line-height: 1;
  }

  .tube__band {
    position: absolute; left: 134px; top: 208px; width: 57px; height: 238px;
    background: var(--band);
  }
  .tube__product {
    position: absolute; left: 50%; bottom: 12px;
    transform-origin: left center;
    transform: translateX(13px) rotate(-90deg);
    white-space: nowrap;
    font-family: "Raleway", sans-serif; font-weight: 300;
    font-size: 24px; letter-spacing: 1px; color: var(--band-text);
  }

  .tube__cap {
    position: absolute; top: 460px; left: 52px; width: 116px; height: 42px;
    background: var(--cap); border-radius: 6px 6px 10px 10px;
  }
</style>
</head>
<body>
  <main class="range">
    <article class="tube tube--shampoo">
      <div class="tube__seal"></div>
      <div class="tube__body">
        <div class="tube__fill"></div>
        <div class="tube__vine" role="img" aria-label="Teal line-drawn leafy vine"></div>
        <div class="tube__sprig" role="img" aria-label="Teal line-drawn leaf sprig"></div>
        <h2 class="tube__brand">Orventa</h2>
        <div class="tube__band"><span class="tube__product">SHAMPOO</span></div>
      </div>
      <div class="tube__cap"></div>
    </article>

    <article class="tube tube--conditioner">
      <div class="tube__seal"></div>
      <div class="tube__body">
        <div class="tube__fill"></div>
        <div class="tube__vine" role="img" aria-label="Teal line-drawn leafy vine"></div>
        <div class="tube__sprig" role="img" aria-label="Teal line-drawn leaf sprig"></div>
        <h2 class="tube__brand">Orventa</h2>
        <div class="tube__band"><span class="tube__product">CONDITIONER</span></div>
      </div>
      <div class="tube__cap"></div>
    </article>

    <article class="tube tube--shower">
      <div class="tube__seal"></div>
      <div class="tube__body">
        <div class="tube__fill"></div>
        <div class="tube__vine" role="img" aria-label="Teal line-drawn leafy vine"></div>
        <div class="tube__sprig" role="img" aria-label="Teal line-drawn leaf sprig"></div>
        <h2 class="tube__brand">Orventa</h2>
        <div class="tube__band"><span class="tube__product">SHOWER GEL</span></div>
      </div>
      <div class="tube__cap"></div>
    </article>

    <article class="tube tube--lotion">
      <div class="tube__seal"></div>
      <div class="tube__body">
        <div class="tube__fill"></div>
        <div class="tube__vine" role="img" aria-label="Teal line-drawn leafy vine"></div>
        <div class="tube__sprig" role="img" aria-label="Teal line-drawn leaf sprig"></div>
        <h2 class="tube__brand">Orventa</h2>
        <div class="tube__band"><span class="tube__product">BODY LOTION</span></div>
      </div>
      <div class="tube__cap"></div>
    </article>
  </main>
</body>
</html>
```